tovrin company need business card, envelope and letterhead design

Check on the attached file wherein you can find our logo and information about the company
Business card will double sided English version and Arabic version

Industry/Entity Type

Business

Requirements
Must have
• include the design also for the letterhead and envelop
Nice to have

```html
<!DOCTYPE html>
<html lang="en">
<head>
<meta charset="utf-8">
<title>Tovrin Stationery</title>
<link href="https://fonts.googleapis.com/css2?family=Open+Sans:wght@400;600;700&display=swap" rel="stylesheet">
<style>
  :root {
    --brand-blue: #1576c0;
    --paper: #ffffff;
    --backdrop: #ebebeb;
    --ink: #3a3a3a;
    --rule: #9a9a9a;
  }
  * { margin: 0; padding: 0; box-sizing: border-box; }
  html, body { width: 1200px; height: 1000px; overflow: hidden; }
  body {
    position: relative;
    background: var(--backdrop);
    font-family: "Open Sans", Arial, sans-serif;
    color: var(--ink);
  }
  .sheet {
    position: absolute;
    background: var(--paper);
    box-shadow: 0 2px 8px rgba(0,0,0,0.12);
  }
  .brand {
    position: absolute;
    display: flex;
    align-items: center;
    gap: 6px;
    color: var(--brand-blue);
    font-weight: 700;
    letter-spacing: 0.5px;
  }
  .brand-square { background: var(--brand-blue); display: block; }
  .brand-on-blue { color: var(--paper); }
  .brand-on-blue .brand-square { background: var(--paper); }

  .letterhead { left: 102px; top: 185px; width: 468px; height: 606px; }
  .letterhead .brand { left: 30px; top: 46px; font-size: 17px; }
  .letterhead .brand-square { width: 16px; height: 16px; }
  .contact-block {
    position: absolute;
    border-left: 1px solid var(--rule);
    padding-left: 9px;
    font-size: 7px;
    line-height: 9px;
  }
  .letterhead .contact-block { left: 315px; top: 32px; height: 53px; }
  .contact-line { display: flex; align-items: center; gap: 3px; }
  .contact-gap { height: 4px; }
  .icon { width: 6px; height: 6px; fill: var(--brand-blue); flex: none; }

  .card-front { left: 642px; top: 185px; width: 217px; height: 123px; }
  .card-front .brand { left: 16px; top: 52px; font-size: 11px; gap: 4px; }
  .card-front .brand-square { width: 10px; height: 10px; }
  .card-front .contact-block {
    left: 102px; top: 28px; height: 66px;
    padding-left: 6px; font-size: 4.6px; line-height: 6px;
  }
  .holder-name { color: var(--brand-blue); font-weight: 700; font-size: 6.6px; line-height: 8px; }
  .card-front .icon { width: 4px; height: 4px; }
  .card-front .contact-gap { height: 3px; }

  .card-back { left: 874px; top: 185px; width: 212px; height: 123px; background: var(--brand-blue); }
  .card-back .brand { left: 44px; top: 50px; font-size: 17px; }
  .card-back .brand-square { width: 16px; height: 16px; }

  .envelope-front { left: 641px; top: 362px; width: 445px; height: 202px; }
  .envelope-front .brand { left: 19px; top: 24px; font-size: 13px; gap: 5px; }
  .envelope-front .brand-square { width: 12px; height: 12px; }
  .return-address { position: absolute; left: 19px; top: 56px; font-size: 5.8px; line-height: 7.6px; }

  .envelope-back { left: 641px; top: 590px; width: 451px; height: 208px; }
  .envelope-flap { position: absolute; left: 0; top: 0; width: 451px; height: 66px; }
</style>
</head>
<body>
  <section class="sheet letterhead">
    <div class="brand"><span class="brand-square"></span>TOVRIN</div>
    <div class="contact-block">
      <div>Nakheel Road - Al Wurud</div>
      <div>P.O. Box 4312-11564</div>
      <div>Kingdom of Saudi Arabia</div>
      <div class="contact-gap"></div>
      <div class="contact-line"><svg class="icon" viewBox="0 0 10 10"><path d="M2 0l2 2-1 1.5c.8 1.6 1.9 2.7 3.5 3.5L8 6l2 2-1.5 2C4 10 0 6 0 1.5z"/></svg>011 2283470</div>
      <div class="contact-line"><svg class="icon" viewBox="0 0 10 10"><path d="M2 0h6v3H2zM0 3.5h10V8H8v2H2V8H0zM3 6.5v2.5h4V6.5z"/></svg>011 2283 471</div>
      <div class="contact-line"><svg class="icon" viewBox="0 0 10 10"><path d="M0 2h10v6H0zM0 2l5 3.5L10 2v1L5 6.5 0 3z"/></svg>tovrin.sa@mail.com</div>
    </div>
  </section>

  <section class="sheet card-front">
    <div class="brand"><span class="brand-square"></span>TOVRIN</div>
    <div class="contact-block">
      <div class="holder-name">Faris Bin Omar Al Rashidi</div>
      <div>General Manager</div>
      <div class="contact-line"><svg class="icon" viewBox="0 0 10 10"><path d="M2 0l2 2-1 1.5c.8 1.6 1.9 2.7 3.5 3.5L8 6l2 2-1.5 2C4 10 0 6 0 1.5z"/></svg>+966 500 318 742</div>
      <div class="contact-gap"></div>
      <div>Nakheel Road - Al Wurud</div>
      <div>P.O. Box 4312-11564</div>
      <div>Kingdom of Saudi Arabia</div>
      <div class="contact-gap"></div>
      <div class="contact-line"><svg class="icon" viewBox="0 0 10 10"><path d="M2 0l2 2-1 1.5c.8 1.6 1.9 2.7 3.5 3.5L8 6l2 2-1.5 2C4 10 0 6 0 1.5z"/></svg>011 2283470</div>
      <div class="contact-line"><svg class="icon" viewBox="0 0 10 10"><path d="M2 0h6v3H2zM0 3.5h10V8H8v2H2V8H0zM3 6.5v2.5h4V6.5z"/></svg>011 2283 471</div>
      <div class="contact-line"><svg class="icon" viewBox="0 0 10 10"><path d="M0 2h10v6H0zM0 2l5 3.5L10 2v1L5 6.5 0 3z"/></svg>tovrin.sa@mail.com</div>
    </div>
  </section>

  <section class="sheet card-back">
    <div class="brand brand-on-blue"><span class="brand-square"></span>TOVRIN</div>
  </section>

  <section class="sheet envelope-front">
    <div class="brand"><span class="brand-square"></span>TOVRIN</div>
    <div class="return-address">
      <div>Nakheel Road - Al Wurud</div>
      <div>P.O. Box 4312-11564</div>
      <div>Kingdom of Saudi Arabia</div>
    </div>
  </section>

  <section class="sheet envelope-back">
    <svg class="envelope-flap" viewBox="0 0 451 66" aria-hidden="true">
      <path d="M0 0H451L441 50Q438 64 424 64H26Q12 64 10 50Z" fill="var(--brand-blue)"/>
      <rect x="216" y="24" width="18" height="18" fill="var(--paper)"/>
    </svg>
  </section>
</body>
</html>
```